Tillard Environmental Projects New Website Design

I need a new website for a Environmental Project Company based in Sydney Australia, working throughout South East Asia.I've attached the company logo, please try & incorporate these colours or use complimentary colours. I've attached a word doc with design brief.I'm going to use Wix, so please ensure files are suitable.Thankyou.

Number of Pages Required

5+ page

Colors

Designer to choose colors to be used in the design.

Requirements
Must have
• Refer to Word Document
Nice to have
• Refer to Word Document
Should not have
• Not to be dark

```html
<!DOCTYPE html>
<html lang="en">
<head>
<meta charset="utf-8">
<title>Tillard Environmental Projects — Home</title>
<link href="https://fonts.googleapis.com/css2?family=Exo+2:wght@300;400;500;700;800&family=Fira+Sans:wght@400;500&display=swap" rel="stylesheet">
<style>
:root{
  --leaf:#4ee07c;
  --mint:#43f17f;
  --forest:#2f5d10;
  --forest-deep:#2d5a14;
  --ink:#1f2a1a;
  --grey:#555c52;
  --white:#ffffff;
  --nav:#1d4a12;
}
*{margin:0;padding:0;box-sizing:border-box}
html,body{width:1200px;height:1200px;overflow:hidden;background:var(--white)}
body{position:relative;font-family:"Fira Sans",sans-serif;color:var(--ink)}
.hero{position:absolute;left:0;top:0;width:1200px;height:511px;overflow:hidden}
.hero-photo{position:absolute;inset:0;
  background:
    radial-gradient(circle at 830px 250px,#e9fbe0 0,#c8f2b4 90px,#8fd86a 170px,transparent 200px),
    radial-gradient(ellipse at 180px 80px,#eaf7d8 0,transparent 260px),
    radial-gradient(ellipse at 600px 430px,#3eb62c 0,transparent 380px),
    linear-gradient(180deg,#b6e59b 0%,#79cf4e 40%,#2f9b23 75%,#1f6e18 100%)}
.nav{position:absolute;top:54px;display:flex;gap:14px;font-family:"Exo 2",sans-serif;font-weight:700;font-size:8.5px;color:var(--nav)}
.nav a{color:inherit;text-decoration:none;position:relative}
.nav a.active{color:#2bb24c}
.nav a.active::after{content:"";position:absolute;left:0;right:0;bottom:-6px;height:1.5px;background:var(--leaf)}
.nav-left{left:364px}
.nav-right{left:707px}
.brand{position:absolute;left:508px;top:30px;display:flex;align-items:center;gap:10px}
.brand-mark{width:62px;height:62px;border-radius:50%;background:#2b6e1c}
.brand-name{font-family:"Exo 2",sans-serif;font-weight:500;font-size:11px;line-height:15px;letter-spacing:.6px;color:#1f5c16;text-transform:uppercase;white-space:nowrap}
.brand-name span{display:block}
.social{position:absolute;left:790px;top:29px;display:flex;gap:5px}
.social span{width:18px;height:18px;border-radius:50%;background:#122010}
.vision{position:absolute;left:303px;top:163px;width:300px}
.vision h1{font-family:"Exo 2",sans-serif;font-weight:500;font-size:33px;color:var(--leaf);line-height:1}
.vision p{margin-top:10px;font-size:9.6px;line-height:13.6px;color:#fff;font-family:"Exo 2",sans-serif;font-weight:500}
.scroll-cue{position:absolute;left:593px;top:474px}
.intro{position:absolute;left:0;top:511px;width:1200px;height:304px;background:var(--white)}
.planet{position:absolute;left:285px;top:10px;width:280px;height:290px;border-radius:46% 50% 48% 52%;
  background:radial-gradient(circle at 55% 50%,#7fd24a 0,#4fb032 45%,#3b9c2a 70%,#8fc6e4 100%)}
.quote{position:absolute;left:613px;top:40px;width:340px;height:250px}
.quote-open{position:absolute;left:0;top:0}
.quote-close{position:absolute;left:257px;top:200px}
.quote-rule{position:absolute;left:262px;top:58px;width:75px;height:1px;background:#d9d9d9}
.quote p{position:absolute;left:59px;top:42px;width:238px;font-family:"Exo 2",sans-serif;font-weight:300;font-size:19.5px;line-height:22.7px;color:var(--ink)}
.focus-band{position:absolute;left:0;top:815px;width:1200px;height:66px;background:var(--mint);display:flex;align-items:center;justify-content:center}
.focus-band h2{font-family:"Exo 2",sans-serif;font-weight:400;font-size:21px;color:#fff}
.focus{position:absolute;left:0;top:881px;width:1200px;height:319px;overflow:hidden;
  background:radial-gradient(ellipse at 600px 120px,#6d9a3c 0,transparent 420px),
  linear-gradient(180deg,#5b8a2e 0%,#3f741c 50%,#2f5e14 100%)}
.card{position:absolute;width:196px;height:183px;background:#fff;box-shadow:0 2px 8px rgba(0,0,0,.25);text-align:center}
.card svg{position:absolute;left:50%;transform:translateX(-50%)}
.card h3{position:absolute;left:0;right:0;font-family:"Exo 2",sans-serif;font-weight:800;font-size:14.5px;line-height:18px;color:var(--forest);letter-spacing:.3px}
.card h3.one-line{top:88px}
.card h3.two-line{top:81px}
.card .rule{position:absolute;left:89px;width:19px;height:1.5px;background:var(--leaf);top:122px}
.card p{position:absolute;left:0;right:0;top:130px;font-size:8.8px;line-height:13.3px;color:var(--grey)}
.row1{top:40px}
.row2{top:266px}
.c1{left:270px}.c2{left:504px}.c3{left:739px}
</style>
</head>
<body>
<header class="hero">
  <div class="hero-photo" role="img" aria-label="Glass globe resting on moss among bright green ferns"></div>
  <nav class="nav nav-left"><a class="active" href="#">Home</a><a href="#">Who we are</a><a href="#">Services</a></nav>
  <div class="brand"><span class="brand-mark"></span><span class="brand-name"><span>Tillard</span><span>Environmental</span><span>Projects</span></span></div>
  <nav class="nav nav-right"><a href="#">Products</a><a href="#">News</a><a href="#">Contact</a></nav>
  <div class="social"><span></span><span></span><span></span></div>
  <section class="vision">
    <h1>Our Vision</h1>
    <p>Our Vision is to make it easy for everyone to minimise their environmental impact by providing information, technology, packaged green solutions &amp; helping innovation flourish.</p>
  </section>
  <svg class="scroll-cue" width="14" height="30" viewBox="0 0 14 30"><rect x="2" y="1" width="10" height="19" rx="5" fill="none" stroke="#fff" stroke-width="1.3"/><line x1="7" y1="5" x2="7" y2="9" stroke="#fff" stroke-width="1.3"/><path d="M5 24l2 2 2-2" fill="none" stroke="#fff" stroke-width="1"/></svg>
</header>

<section class="intro">
  <div class="planet" role="img" aria-label="Illustrated small planet with city, fields, river and trees"></div>
  <blockquote class="quote">
    <svg class="quote-open" width="54" height="36" viewBox="0 0 54 36"><g fill="var(--leaf)"><circle cx="11" cy="24" r="11"/><path d="M1 24C1 10 10 3 18 2l1 3C12 7 8 13 9 20z"/><circle cx="41" cy="24" r="11"/><path d="M31 24C31 10 40 3 48 2l1 3C42 7 38 13 39 20z"/></g></svg>
    <span class="quote-rule"></span>
    <p>Working with people to minimise the environmental impact of humans on the earth without sacrificing lifestyle and helping innovation flourish.</p>
    <svg class="quote-close" width="54" height="36" viewBox="0 0 54 36"><g fill="var(--leaf)"><circle cx="11" cy="12" r="11"/><path d="M21 12C21 26 12 33 4 34l-1-3C10 29 14 23 13 16z"/><circle cx="41" cy="12" r="11"/><path d="M51 12C51 26 42 33 34 34l-1-3C40 29 44 23 43 16z"/></g></svg>
  </blockquote>
</section>

<div class="focus-band"><h2>We will achieve this by focusing on the following</h2></div>

<section class="focus" role="group" aria-label="Focus areas">
  <article class="card row1 c1">
    <svg style="top:20px" width="56" height="56" viewBox="0 0 56 56" fill="none" stroke="var(--forest-deep)" stroke-width="1.6"><path d="M20 10l8-5 8 8"/><path d="M36 13l-4 1M36 13l1-4"/><path d="M46 24l3 10-6 9h-9"/><path d="M34 43l3-3M34 43l3 3"/><path d="M18 46H10l-4-9 5-9"/><path d="M11 28l-4 1M11 28l1 4"/></svg>
    <h3 class="one-line">SUSTAINABLE FOOD</h3>
    <span class="rule"></span>
    <p>Lorem ipsum dolor sit amet,<br>consectetur adipiscing elit.<br>Vivamus vel turpis felis.</p>
  </article>
  <article class="card row1 c2">
    <svg style="top:14px" width="62" height="58" viewBox="0 0 62 58" fill="none" stroke="var(--forest-deep)" stroke-width="1.4"><circle cx="14" cy="14" r="6"/><path d="M14 3v3M5 14h3M7 7l2 2M21 7l-2 2"/><path d="M14 24L22 46H58L50 24Z"/><path d="M18 35h36M27 24l3 22M36 24l2 22M44 24l3 22"/><path d="M40 46v8M32 54h16"/></svg>
    <h3 class="two-line">SUSTAINABLE /<br>RENEWABLE POWER</h3>
    <span class="rule"></span>
    <p>Lorem ipsum dolor sit amet,<br>consectetur adipiscing elit.<br>Vivamus vel turpis felis.</p>
  </article>
  <article class="card row1 c3">
    <svg style="top:16px" width="84" height="50" viewBox="0 0 84 50" fill="none" stroke="var(--forest-deep)" stroke-width="1.6"><path d="M42 4C36 14 32 19 32 25a10 10 0 0 0 20 0c0-6-4-11-10-21z"/><path d="M45 21c1 3 0 7-3 8"/><ellipse cx="42" cy="38" rx="40" ry="9"/><ellipse cx="42" cy="36" rx="26" ry="5" stroke-dasharray="8 3"/></svg>
    <h3 class="two-line">WATER QUALITY &amp;<br>TREATMENT</h3>
    <span class="rule"></span>
    <p>Lorem ipsum dolor sit amet,<br>consectetur adipiscing elit.<br>Vivamus vel turpis felis.</p>
  </article>
  <article class="card row2 c1">
    <svg style="top:26px" width="66" height="30" viewBox="0 0 66 30" fill="none" stroke="var(--forest-deep)" stroke-width="1.6"><path d="M6 29c-4-8 2-14 9-12 1-8 10-12 17-8 4-6 16-5 17 4 8-1 14 7 11 16"/></svg>
  </article>
  <article class="card row2 c2">
    <svg style="top:12px" width="44" height="44" viewBox="0 0 44 44" fill="none" stroke="var(--forest-deep)" stroke-width="1.6"><rect x="6" y="2" width="32" height="6" rx="2"/><path d="M8 8l2 34h24l2-34"/><path d="M22 20c-6 6-4 12 0 14 4-2 6-8 0-14z"/></svg>
  </article>
  <article class="card row2 c3">
    <svg style="top:12px" width="70" height="50" viewBox="0 0 70 50" fill="none" stroke="var(--forest-deep)" stroke-width="1.6"><ellipse cx="35" cy="30" rx="30" ry="10" transform="rotate(-25 35 30)"/><ellipse cx="35" cy="30" rx="30" ry="10" transform="rotate(25 35 30)"/><ellipse cx="35" cy="30" rx="10" ry="28"/><circle cx="35" cy="30" r="4"/></svg>
  </article>
</section>
</body>
</html>
```